Bulldog themed background for Real Estate Purchase Letter

I need a phantom background or watermark on a standard 8 1/2" x 11" paper. I am going to put a letter over the background. I want a bulldog theme that is cute, funny and original. This letter is for a real estate project and we want to capture the person sub-consciously . Attached is my personal dogs. If you want to use them you can but not required. I have attached the letter that I am trying to emulate. I want bulldogs not horses.

Target Market(s)

45 years old and higher

Industry/Entity Type

Real Estate

Font styles to use
Serif
Sans Serif

Colors

Designer to choose colors to be used in the design.

Requirements
Must have
• fun, happiness, reassuring,
Should not have
• violence, negativity, unhappy

```html
<!DOCTYPE html>
<html lang="en">
<head>
<meta charset="utf-8">
<title>Real Estate Purchase Letter</title>
<link href="https://fonts.googleapis.com/css2?family=Montserrat:wght@500&family=Open+Sans:wght@400;600&display=swap" rel="stylesheet">
<style>
  :root {
    --blue-deep: #0a4fc4;
    --blue-mid: #1f74e0;
    --cyan: #17b3ef;
    --paper: #ffffff;
    --ink: #3a3a3a;
    --ink-strong: #2f2f2f;
    --dog-cream: #efe9e2;
    --dog-shadow: #d9d2cb;
    --dog-rose: #d9a6a8;
  }
  * { margin: 0; padding: 0; box-sizing: border-box; }
  html, body { width: 850px; height: 1200px; overflow: hidden; background: var(--paper); }
  .letterhead {
    position: relative;
    width: 850px;
    height: 1200px;
    background: var(--paper);
    font-family: "Open Sans", Arial, sans-serif;
    color: var(--ink);
    overflow: hidden;
  }
  .wave { position: absolute; left: 0; top: 0; width: 850px; height: 1200px; }
  .mascot-watermark {
    position: absolute;
    left: 70px;
    top: 115px;
    width: 700px;
    height: 1040px;
    border-radius: 48% 48% 40% 40%;
    background:
      radial-gradient(ellipse 40% 18% at 50% 50%, rgba(217,166,168,0.45), transparent 70%),
      radial-gradient(ellipse 60% 50% at 50% 40%, var(--dog-cream), rgba(239,233,226,0.6) 60%, transparent 80%),
      radial-gradient(ellipse 50% 30% at 50% 85%, rgba(217,210,203,0.5), transparent 75%);
    opacity: 0.75;
  }
  .agent-id {
    position: absolute;
    left: 67px;
    top: 48px;
    font-family: "Montserrat", Arial, sans-serif;
    font-weight: 500;
    font-size: 17.5px;
    line-height: 24px;
    color: var(--paper);
  }
  .letter-body {
    position: absolute;
    left: 69px;
    top: 197px;
    width: 711px;
    font-size: 17.5px;
    line-height: 32.7px;
  }
  .recipient { line-height: 30px; }
  .recipient .name, .salutation strong, .highlight, .signature { font-weight: 600; color: var(--ink-strong); }
  .salutation { margin-top: 40px; }
  .letter-body p.paragraph { text-indent: 40px; text-align: justify; }
  .p1 { margin-top: 35px; }
  .p2, .p3 { margin-top: 36px; }
  .closing { margin-top: 40px; }
  .signature { margin-top: 40px; }
</style>
</head>
<body>
  <main class="letterhead">
    <div class="mascot-watermark" role="img" aria-label="Faint watermark photo of a happy white bulldog with its tongue out"></div>

    <svg class="wave" viewBox="0 0 850 1200" aria-hidden="true">
      <path d="M0 0 H560 C500 25 440 45 380 75 C280 125 170 115 75 170 C40 190 15 215 0 245 Z" fill="var(--cyan)"/>
      <path d="M0 0 H540 C480 20 420 38 360 66 C260 112 150 102 60 152 C30 170 10 195 0 222 Z" fill="var(--blue-deep)"/>
      <path d="M180 1200 C320 1185 410 1120 520 1092 C650 1060 770 1060 850 940 V1200 Z" fill="var(--cyan)"/>
      <path d="M210 1200 C340 1190 430 1135 535 1110 C660 1080 775 1085 850 975 V1200 Z" fill="var(--blue-mid)"/>
      <path d="M260 1200 C380 1195 470 1150 570 1130 C690 1105 790 1110 850 1030 V1200 Z" fill="var(--blue-deep)"/>
    </svg>

    <div class="agent-id">Real Estate Agent ID :<br>#0127384950</div>

    <article class="letter-body">
      <address class="recipient" style="font-style:normal">
        <span class="name">Mr. Outta Stateowner</span><br>
        123456 Main Street<br>
        Larkfield FL 3440-5360
      </address>

      <p class="salutation">Dear <strong>First Name</strong></p>

      <p class="paragraph p1">I am writing you, because I am interested in purchasing your property located at <span class="highlight">123456 Main Street Larkfield FL 3440-5360</span> I live nearby in Pinecrest Hollow and I puschages properties throught the state of PA Currently I am working on projects in the neighbourhood, which is how I learned of your property.</p>

      <p class="paragraph p2">Please call me at <span class="highlight">(XXX) XXXX-Local#</span> so I can tell you how we can buy your property quickly, with no hassels and most importantly, at a fair price. I purchase the hous directly from you so there are no real estate commissions or extra fees coming out of your pocket. Furthermore, I always make cash offers so you never have to worry about delays resulting from a buyer trying to qualify for a mortgage and wasting your valuable time.</p>

      <p class="paragraph p3">I'will be glade to personally tell you more about how we can work together. All call are completely confidential and there is no obligation whatsoever. Even if you are not intersted in selling at thing time call <span class="highlight">(xxx) xxxx-xxxx</span>, so I can help you with determining the value of your property. You should also keep this letter for your future reference, since things in life have a tendency to change unexpectedly. Thanks you for your time and consideration and I look forward to speaking with you.</p>

      <p class="closing">Sincerely,</p>
      <p class="signature">Carla Benson</p>
    </article>
  </main>
</body>
</html>
```